TORNWICK Pizza Flyer / Menu

Hello so its a new pizza shop called Tornwick. I need a flyer menu designed . it will be 30cm tall and 10.5cm wide. i made one which i have uploaded but as you can see im not very skillfull design wise. I did want the logo on the front with the photo of the counter in the middle and then half the pizza at the bottom. then on the back i wanted all the different toppings ( doesnt have to be the same pics as i have used ) and then drinks and desserts underneath and our contact details. I dont want to include our signature specials. Also facebook/twitter and instagram logos somewhere. the font i have been using is called 'AR CENA' i have attached a rough sketch i have put together to give you an idea too. thanks

Industry/Entity Type

Shop

```html
<!DOCTYPE html>
<html lang="en">
<head>
<meta charset="utf-8">
<title>Tornwick Pizza Menu</title>
<link rel="stylesheet" href="https://fonts.googleapis.com/css2?family=Alfa+Slab+One&family=Roboto+Slab:wght@400;700;800&family=Montserrat:wght@800;900&display=swap">
<style>
:root{
  --night:#262524;
  --night-deep:#1b1a19;
  --orange:#f39200;
  --band:#1e1d1c;
  --cream:rgba(255,241,224,.78);
  --wood-light:#d79a5c;
  --wood-dark:#b0703a;
  --ink:#1c1c1c;
  --yellow:#ffd21a;
  --ribbon:#e8501e;
  --social:#2f6db5;
  --white:#ffffff;
}
*{margin:0;padding:0;box-sizing:border-box}
html,body{width:1200px;height:3429px;overflow:hidden}
body{background:linear-gradient(180deg,var(--night) 0%,var(--night-deep) 100%);position:relative;font-family:"Roboto Slab",serif;color:var(--ink)}
.abs{position:absolute}

.header-frame{left:240px;top:96px;width:754px;height:293px;border:4px solid var(--white)}
.brand-dot{left:272px;top:232px;width:84px;height:84px;border-radius:50%;background:var(--orange)}
.address{left:380px;top:176px;font-family:"Roboto Slab",serif;font-weight:700;font-size:23px;color:var(--orange);letter-spacing:1px}
.brand-name{left:376px;top:206px;font-family:"Roboto Slab",serif;font-weight:700;font-size:100px;line-height:1.1;color:var(--white);letter-spacing:2px}
.established{left:860px;top:330px;font-family:"Roboto Slab",serif;font-weight:700;font-size:17px;color:var(--white);letter-spacing:1px}

.board{left:80px;top:491px;width:1040px;height:2938px;border-radius:40px 40px 0 0;background:linear-gradient(100deg,var(--wood-dark) 0%,var(--wood-light) 35%,var(--wood-dark) 70%,var(--wood-light) 100%)}
.greens-lime{left:0;top:1965px;width:140px;height:330px;border-radius:0 160px 160px 0;background:radial-gradient(circle at 30% 50%,#c8dc5a,#6f9a2a)}
.greens-leaf{left:0;top:2380px;width:120px;height:640px;border-radius:0 90px 90px 0;background:linear-gradient(180deg,#5f9a35,#3a6e24)}

.band{left:80px;width:697px;height:69px;background:var(--band);color:var(--white);font-family:"Alfa Slab One",serif;font-size:35px;line-height:69px;padding-left:60px;letter-spacing:1px}

.panel{left:114px;width:960px;background:var(--cream);border-radius:14px}
.how-list{top:626px;height:192px;padding:16px 40px 16px 30px;font-family:"Roboto Slab",serif;font-size:30px;line-height:38px;list-style:none}
.how-list li{padding-left:22px;text-indent:-22px}
.how-list li::before{content:"• "}

.price-badge{left:759px;top:821px;width:128px;height:128px;border-radius:50%;background:var(--white);border:9px solid var(--orange);font-family:"Alfa Slab One",serif;font-size:36px;line-height:110px;text-align:center;color:var(--ink)}

.topping{width:137px;text-align:center}
.topping .tile{width:137px;height:137px;background:var(--white);padding:9px;border-radius:6px;box-shadow:0 6px 10px rgba(0,0,0,.35)}
.topping .tile span{display:block;width:100%;height:100%;border-radius:3px}
.topping p{margin:8px -8px 0;font-family:"Roboto Slab",serif;font-weight:800;font-size:15px;line-height:16px;color:var(--ink);text-transform:uppercase}

.menu-list{list-style:none;padding:14px 24px}
.menu-list li{display:flex;align-items:flex-end;font-family:"Roboto Slab",serif;font-weight:700;font-size:31px;line-height:48px;color:var(--ink)}
.menu-list li::before{content:"•";margin-right:8px}
.menu-list .leader{flex:1;border-bottom:2px solid var(--ink);margin:0 10px 12px}
.menu-list .price{font-family:"Montserrat",sans-serif;font-weight:800;font-style:italic;font-size:27px}
.legendary{display:inline-block;margin:0 0 10px 30px;padding:0 12px;height:44px;background:var(--yellow);border:3px solid var(--ribbon);color:var(--ribbon);font-family:"Roboto Slab",serif;font-weight:800;font-size:24px;line-height:38px;transform:rotate(-3deg)}

.delivery{left:80px;width:1040px;text-align:center;font-family:"Montserrat",sans-serif;font-weight:900;color:var(--yellow);font-size:44px;line-height:58px}
.min-order{left:80px;top:3140px;width:1040px;text-align:center;font-family:"Montserrat",sans-serif;font-weight:800;color:var(--white);font-size:27px}
.ribbon{left:150px;top:3192px}
.phone{left:150px;top:3192px;width:900px;height:116px;text-align:center;font-family:"Montserrat",sans-serif;font-weight:900;color:var(--white);font-size:84px;line-height:116px}

.social{top:3333px;width:66px;height:66px;border-radius:8px;background:var(--social)}
.follow{left:503px;top:3342px;width:560px;font-family:"Montserrat",sans-serif;font-weight:800;color:var(--white);font-size:15px;line-height:19px}
</style>
</head>
<body>

<div class="abs header-frame"></div>
<div class="abs brand-dot"></div>
<div class="abs address">14 KILN ROW, ASHBRIDGE, AB2 7QT</div>
<div class="abs brand-name">TORNWICK</div>
<div class="abs established">EST. 2016</div>

<div class="abs board" role="img" aria-label="Wooden serving board texture"></div>
<div class="abs greens-lime" role="img" aria-label="Photo of a lime wedge"></div>
<div class="abs greens-leaf" role="img" aria-label="Photo of fresh lettuce leaves"></div>

<div class="abs band" style="top:530px">HOW DO YOU GET BLAZED?</div>
<ul class="abs panel how-list">
  <li>Buld your own, or choose one of ours</li>
  <li>Add as many topping as you like, all one price</li>
  <li>We blaze it in 150 seconds so stay close and listen for your name</li>
</ul>

<div class="abs band" style="top:850px">BUILD IT!</div>
<div class="abs price-badge">6,99</div>

<div class="abs topping" style="left:142px;top:949px"><div class="tile"><span role="img" aria-label="Photo of pineapple chunks" style="background:#f2c230"></span></div><p>Pineapple</p></div>
<div class="abs topping" style="left:297px;top:949px"><div class="tile"><span role="img" aria-label="Photo of pepperoni slices" style="background:#d9542b"></span></div><p>Pepperoni</p></div>
<div class="abs topping" style="left:452px;top:949px"><div class="tile"><span role="img" aria-label="Photo of red pepper" style="background:#c8201c"></span></div><p>Red pepper</p></div>
<div class="abs topping" style="left:607px;top:949px"><div class="tile"><span role="img" aria-label="Photo of black olives" style="background:#1a1a22"></span></div><p>Black olive</p></div>
<div class="abs topping" style="left:762px;top:949px"><div class="tile"><span role="img" aria-label="Photo of spinach" style="background:#4f8a30"></span></div><p>Spinach</p></div>
<div class="abs topping" style="left:917px;top:949px"><div class="tile"><span role="img" aria-label="Photo of garlic cloves" style="background:#e6dccb"></span></div><p>Garlic</p></div>

<div class="abs topping" style="left:142px;top:1143px"><div class="tile"><span role="img" aria-label="Photo of grated mozzarella" style="background:#eedfa8"></span></div><p>Mozarella</p></div>
<div class="abs topping" style="left:297px;top:1143px"><div class="tile"><span role="img" aria-label="Photo of green olives" style="background:#b3b032"></span></div><p>Green olive</p></div>
<div class="abs topping" style="left:452px;top:1143px"><div class="tile"><span role="img" aria-label="Photo of ricotta" style="background:#eeeae2"></span></div><p>Ricotta</p></div>
<div class="abs topping" style="left:607px;top:1143px"><div class="tile"><span role="img" aria-label="Photo of green pepper" style="background:#3d8f1f"></span></div><p>Green pepper</p></div>
<div class="abs topping" style="left:762px;top:1143px"><div class="tile"><span role="img" aria-label="Photo of red onion" style="background:#8a3f6b"></span></div><p>Onion</p></div>
<div class="abs topping" style="left:917px;top:1143px"><div class="tile"><span role="img" aria-label="Photo of grated cheddar" style="background:#f0a22a"></span></div><p>Cheddar<br>cheese</p></div>

<div class="abs topping" style="left:142px;top:1333px"><div class="tile"><span role="img" aria-label="Photo of basil leaves" style="background:#3f8e34"></span></div><p>Basil</p></div>
<div class="abs topping" style="left:297px;top:1333px"><div class="tile"><span role="img" aria-label="Photo of pulled chicken" style="background:#b89a78"></span></div><p>Pulled<br>chiken</p></div>
<div class="abs topping" style="left:452px;top:1333px"><div class="tile"><span role="img" aria-label="Photo of pulled beef" style="background:#9a6a50"></span></div><p>Pulled<br>beff</p></div>
<div class="abs topping" style="left:607px;top:1333px"><div class="tile"><span role="img" aria-label="Photo of sliced mushrooms" style="background:#d6ccb6"></span></div><p>Mushroom</p></div>
<div class="abs topping" style="left:762px;top:1333px"><div class="tile"><span role="img" aria-label="Photo of cherry tomatoes" style="background:#d8481e"></span></div><p>Tomato</p></div>
<div class="abs topping" style="left:917px;top:1333px"><div class="tile"><span role="img" aria-label="Photo of salami slices" style="background:#b4555a"></span></div><p>Salami</p></div>

<div class="abs topping" style="left:142px;top:1513px"><div class="tile"><span role="img" aria-label="Photo of capers" style="background:#8a9a3a"></span></div><p>Capers</p></div>
<div class="abs topping" style="left:297px;top:1513px"><div class="tile"><span role="img" aria-label="Photo of anchovies" style="background:#a07a4a"></span></div><p>Anchovies</p></div>
<div class="abs topping" style="left:452px;top:1513px"><div class="tile"><span role="img" aria-label="Photo of jalapeno slices" style="background:#3f7a22"></span></div><p>Jalapenos</p></div>
<div class="abs topping" style="left:607px;top:1513px"><div class="tile"><span role="img" aria-label="Photo of sweetcorn" style="background:#e8b820"></span></div><p>Corn</p></div>
<div class="abs topping" style="left:762px;top:1513px"><div class="tile"><span role="img" aria-label="Photo of dried chillies" style="background:#a8281a"></span></div><p>Chili</p></div>
<div class="abs topping" style="left:917px;top:1513px"><div class="tile"><span role="img" aria-label="Photo of barbecue sauce" style="background:#5a1e14"></span></div><p>B-B-Q</p></div>

<div class="abs topping" style="left:293px;top:1696px"><div class="tile"><span role="img" aria-label="Photo of pesto" style="background:#4e8a2a"></span></div><p>Pesto</p></div>
<div class="abs topping" style="left:448px;top:1696px"><div class="tile"><span role="img" aria-label="Photo of chorizo" style="background:#8a2a1e"></span></div><p>Chorizo</p></div>
<div class="abs topping" style="left:603px;top:1696px"><div class="tile"><span role="img" aria-label="Photo of parmesan wedge" style="background:#e6cc8a"></span></div><p>Parmesan</p></div>
<div class="abs topping" style="left:758px;top:1696px"><div class="tile"><span role="img" aria-label="Photo of sweet chilli sauce" style="background:#e4442a"></span></div><p>Sweet chili</p></div>

<div class="abs band" style="top:1915px">EXTRAS...</div>
<ul class="abs panel menu-list" style="top:2021px;height:208px">
  <li>SIDE SALAD<span class="leader"></span><span class="price">2.49</span></li>
  <li>GARLIC BREAD<span class="leader"></span><span class="price">2.49</span></li>
  <li>GARLIC DREAD WITH CHEESE<span class="leader"></span><span class="price">2.99</span></li>
  <li>OLIVE POT<span class="leader"></span><span class="price">1.49</span></li>
</ul>

<div class="abs band" style="top:2309px">DESERTS...</div>
<ul class="abs panel menu-list" style="top:2416px;height:208px">
  <li>BANANACHOC PIZZA<span class="legendary">LEGENDARY</span><span class="leader"></span><span class="price">3.99</span></li>
  <li>CREME BRULLE<span class="leader"></span><span class="price">2.49</span></li>
  <li>TIRAMISY<span class="leader"></span><span class="price">2.49</span></li>
  <li>CHOCO DREAM CAKE<span class="leader"></span><span class="price">2.49</span></li>
</ul>

<div class="abs band" style="top:2693px">DRINKS...</div>
<ul class="abs panel menu-list" style="top:2800px;height:206px">
  <li>BLOOD ORANGE<span class="leader"></span><span class="price">0.99</span></li>
  <li>ORANGEADE<span class="leader"></span><span class="price">0.99</span></li>
  <li>LEMON<span class="leader"></span><span class="price">0.99</span></li>
  <li>CLASSIC COLA<span class="leader"></span><span class="price">0.89</span></li>
</ul>

<div class="abs delivery" style="top:3026px">WOOD STONE PIZZA DELIVERED</div>
<div class="abs delivery" style="top:3084px">HOT YOUR DOOR STEP</div>
<div class="abs min-order">minimum order £12</div>

<svg class="abs ribbon" width="900" height="116" viewBox="0 0 900 116" aria-hidden="true">
  <polygon points="0,0 900,0 860,58 900,116 0,116 40,58" fill="#e8501e"/>
</svg>
<div class="abs phone">0207 555 0192</div>

<div class="abs social" style="left:229px"></div>
<div class="abs social" style="left:327px"></div>
<div class="abs social" style="left:425px"></div>
<div class="abs follow">FOLLOW US FOR UPDATES, OFFERS AND IF YOUR LUCKY...<br>A FREE PIZZA</div>

</body>
</html>
```